Front cover for Bathroom Catalogue

We want to see some concepts for a new front cover of our next catalogue. Attached is the existing.

The following must be included on the cover:
1. "Corlen Vaska" logo
2. x9 product category Icons (can display just 9 or turn into a pattern like exisiting)
3. Ideally we include the Water Splash Pattern in some capacity, also attached (Feel free to add colour to the splash/edit or incorporate the splash into something else).

We also wish to add some colour/colours to make it stand out from the previous cover too.

Target Market(s)

Home owners, renovators, designers, architects

Industry/Entity Type

Bathroom

Font styles to use
Sans Serif

Colors
0054AA
0677BA
7BADD7
CADEEF
E8F1F8
0094D4
00A9DD
6FCCEA
C7EBF8
E9F6FB

Requirements
Must have
• Colour, "Corlen Vaska" logo, x9 product category icons.
Nice to have
• Possibly some colour to make it stand out.

```html
<!DOCTYPE html>
<html lang="en">
<head>
<meta charset="utf-8">
<title>Corlen Vaska – Bathroom Accessories Catalogue Cover</title>
<link href="https://fonts.googleapis.com/css2?family=Outfit:wght@300;400;700&display=swap" rel="stylesheet">
<style>
  :root {
    --ink: #161616;
    --paper: #eceeef;
    --sky-soft: #c9dcef;
    --sky-pale: #e8f1f8;
    --orbit: #0094d4;
    --rule: #6fcbea;
    --wood-light: #c99a62;
    --wood-dark: #8a6038;
    --stone: #b9b1a6;
    --band: #e9edf1;
  }
  * { margin: 0; padding: 0; box-sizing: border-box; }
  html, body { width: 903px; height: 1200px; overflow: hidden; }
  body {
    font-family: "Outfit", sans-serif;
    color: var(--ink);
    background: var(--paper);
  }
  .cover {
    position: relative;
    width: 903px;
    height: 1200px;
    overflow: hidden;
    background:
      radial-gradient(ellipse 420px 380px at 452px 700px, rgba(255,255,255,0.55), rgba(255,255,255,0) 70%),
      linear-gradient(200deg, var(--sky-soft) 0%, var(--paper) 38%, var(--paper) 70%, var(--sky-pale) 100%);
  }
  .hero-photo {
    position: absolute;
    left: 233px;
    top: 76px;
    width: 437px;
    height: 525px;
    border-radius: 218px 218px 10px 10px;
    background:
      linear-gradient(180deg, rgba(255,255,255,0) 78%, rgba(196,160,110,0.9) 100%),
      linear-gradient(90deg, var(--wood-dark) 0%, var(--wood-light) 30%, #b48656 53%, var(--stone) 54%, #cfc8be 80%, #bdb5aa 100%);
  }
  .orbit {
    position: absolute;
    left: 0;
    top: 0;
    width: 903px;
    height: 1200px;
    pointer-events: none;
  }
  .wordmark {
    position: absolute;
    left: 0;
    width: 100%;
    top: 640px;
    text-align: center;
    font-weight: 300;
    font-size: 92px;
    letter-spacing: 1px;
    line-height: 1;
  }
  .category {
    position: absolute;
    left: 0;
    width: 100%;
    text-align: center;
  }
  .category-lead { top: 858px; font-size: 54px; font-weight: 400; letter-spacing: -0.5px; }
  .category-title { top: 920px; font-size: 57px; font-weight: 700; letter-spacing: -1px; }
  .web { top: 995px; font-size: 25px; font-weight: 300; }
  .rule {
    position: absolute;
    left: 313px;
    top: 1036px;
    width: 277px;
    height: 1px;
    background: var(--rule);
  }
  .issue { top: 1050px; font-size: 17px; font-weight: 400; }
  .years { top: 1070px; font-size: 26px; font-weight: 400; }
  .icon-band {
    position: absolute;
    left: 0;
    top: 1104px;
    width: 100%;
    height: 96px;
    background: linear-gradient(90deg, var(--sky-soft) 0%, var(--band) 35%, var(--band) 100%);
  }
  .icon-row { position: absolute; left: 0; top: 0; }
</style>
</head>
<body>
<main class="cover">
  <div class="hero-photo" role="img" aria-label="Photo of a warm modern bathroom with timber wall panelling, round mirror, floating vanity, pendant lights and a freestanding white bath"></div>

  <svg class="orbit" viewBox="0 0 903 1200" aria-hidden="true">
    <ellipse cx="451" cy="363" rx="400" ry="118" transform="rotate(-27 451 363)" fill="none" stroke="var(--orbit)" stroke-width="1.6"/>
    <g fill="none" stroke="var(--orbit)" stroke-width="1.6" stroke-linejoin="round">
      <path d="M131 592 Q134 614 155 617 Q134 620 131 642 Q128 620 107 617 Q128 614 131 592 Z"/>
      <path d="M700 810 Q703 832 724 835 Q703 838 700 860 Q697 838 676 835 Q697 832 700 810 Z"/>
    </g>
  </svg>

  <div class="wordmark">Corlen Vaska</div>

  <div class="category category-lead">Bathroom</div>
  <div class="category category-title">ACCESSORIES</div>
  <div class="category web">corlenvaska.co.nz</div>
  <div class="rule"></div>
  <div class="category issue">ISSUE 25</div>
  <div class="category years">2023 | 2024</div>

  <div class="icon-band">
    <svg class="icon-row" width="903" height="96" viewBox="0 0 903 96" aria-label="Product categories" role="img">
      <g fill="var(--ink)">
        <!-- basin -->
        <path d="M224 36 h28 v22 h-6 v-8 q-8 0-14-6 z"/><rect x="243" y="29" width="4" height="8"/><rect x="243" y="29" width="9" height="3"/>
        <!-- vanity -->
        <path d="M289 32 h22 v26 h-22 z M292 36 v6 h16 v-6 z M292 45 v6 h16 v-6 z" fill-rule="evenodd"/>
        <!-- bath -->
        <path d="M343 40 h28 v5 q0 8-8 8 h-12 q-8 0-8-8 z"/><rect x="344" y="53" width="3" height="4"/><rect x="367" y="53" width="3" height="4"/>
        <!-- spout -->
        <path d="M393 36 h14 v22 h-5 v-17 h-9 z"/><rect x="393" y="42" width="5" height="3"/>
        <!-- toilet -->
        <path d="M460 30 h5 v28 h-20 v-8 h-4 v-6 h13 v6 h6 z"/>
        <!-- shower head -->
        <circle cx="509" cy="38" r="8"/><rect x="507" y="45" width="4" height="14"/>
        <!-- enclosure -->
        <path d="M547 32 l10-4 l10 4 v26 l-10 4 l-10-4 z" fill="none" stroke="var(--ink)" stroke-width="2"/>
        <line x1="557" y1="28" x2="557" y2="62" stroke="var(--ink)" stroke-width="1.5"/>
        <!-- soap dispenser -->
        <rect x="605" y="40" width="14" height="19" rx="2"/><rect x="609" y="33" width="6" height="7"/><rect x="609" y="31" width="11" height="3"/>
        <!-- mixer -->
        <path d="M664 58 v-14 q0-12 10-12 q8 0 8 8" fill="none" stroke="var(--ink)" stroke-width="3"/><circle cx="664" cy="50" r="4"/>
      </g>
    </svg>
  </div>
</main>
</body>
</html>
```